依頼詳細
ご提案いただきたいのは、A4判チラシとA3判ポスターのデザイン案2点となります。
・A4判(チラシ)
・A3判(ポスター)

添付のWordには以下2点を掲載しています。
・A4判の原稿
・A3判の記載要件

【A4判チラシについて】
A4判の原稿は、簡易的な仮デザインを行っていますが、みなさまのセンスで再構成頂いて構いません。ただし、掲載する要素を減らすことはNGとさせていただきます。
すべての要素を含んでいれば、配置・色などすべてお任せいたします。
色々な案を拝見したいので、イメージ色、品質などの指定はございません。

【A3判ポスターについて】
A3判のポスターにつきましては、添付資料2ページ目に記載要件のみを掲載しています。要件に従ってA4判の原稿から構成要素を抽出して配置して頂くイメージでお願いいたします。
単にA4判をA3判に引き伸ばすのではなく、ポスターとしてのデザインをお願いできれば幸いです。

【補足】
・本コンペの提出形式はjpeg等の画像形式でかまいませんが、当選者様には、伏せている情報などをお伝えして、イラストレーター形式(ai)の完成形にてご提出をお願いする可能性がございます。その際の費用につきましては、別途ご相談(各15,000円前後を想定)させていただきます。本コンペで完了する場合もございます。

・添付資料では伏せております学校名、個人名、住所等の〇や△の記号は、実際の文字数となっております。〇や△を架空の名称に置き換えてデザインいただいても構いません。その方がイメージは沸きやすいので助かります。

短期間ではございますが、どうぞよろしくお願いいたします。
記載項目
学校ロゴ
参加費(無料)
見出し(講座タイトル)
≪概要≫掲載事項
開催日時
参加対象
開催場所(アクセス良好な旨を強調)
eスポーツ競技会概略
申込方法(URL・QRコード・注意事項)
問い合わせ先

サイズ
A4判のチラシ、A3判のポスター
ページ数
片面
希望イメージ
シンプル 複雑
単色 カラフル
暗い 明るい
日常 高級
遊び心 厳粛
未来的 伝統的
女性的 男性的
希望する色
設定なし
納品ファイル
• イラストレーター形式 (.ai)
補足説明
コンペの提出については、高解像度JPG (.jpg)、PNG形式 (.png)で構いません。
当選者様には、イラストレーター形式(ai)の完成形にてご提出をお願いする可能性がございます
各記載項目は、以下となります。

【A4判チラシ】
添付資料1ページ目の要素すべて

【A3判ポスター】
添付資料2ページ目の記載要件

よろしくお願いいたします。

とても目を惹くデザインで、こちらの意向に合致しておりました。

この度は、数多くのご提案をいただき、ありがとうございました。
中には、複数の案をご提出いただいた方もおられます。誠にありがとうございました。
皆様の益々のご活躍を心よりお祈り申し上げます。

```html
<!DOCTYPE html>
<html lang="ja">
<head>
<meta charset="UTF-8">
<title>e-Sports マネジメント人材養成講座</title>
<link rel="stylesheet" href="https://fonts.googleapis.com/css2?family=Montserrat:wght@800;900&family=Noto+Sans+JP:wght@400;500;700;900&display=swap">
<style>
:root{
  --navy:#050b1e;
  --blue:#0c5fb8;
  --cyan:#35c6f4;
  --cyan-light:#b9ecff;
  --yellow:#ffe100;
  --pink:#e4007f;
  --white:#ffffff;
  --ink:#1a1a1a;
  --jp:"Noto Sans JP",sans-serif;
  --en:"Montserrat",sans-serif;
}
*{margin:0;padding:0;box-sizing:border-box}
html,body{width:853px;height:1200px;overflow:hidden;background:var(--navy)}
.flyer{position:relative;width:853px;height:1200px;overflow:hidden;font-family:var(--jp);color:var(--white);background:var(--navy)}
.hero-photo{position:absolute;left:0;top:0;width:853px;height:1010px;
  background:
    radial-gradient(ellipse 260px 380px at 200px 620px,#3a4a6a 0%,rgba(40,55,85,.6) 45%,transparent 75%),
    radial-gradient(ellipse 500px 200px at 430px 40px,#1f5fbf 0%,transparent 70%),
    linear-gradient(180deg,#0d2a66 0%,#081634 35%,var(--navy) 70%,#03060f 100%);}
.lead{position:absolute;left:0;top:45px;width:853px;text-align:center;font-weight:900;font-size:44px;line-height:56px;letter-spacing:1px;text-shadow:0 2px 8px rgba(0,0,0,.7)}
.lead em{font-style:normal;color:var(--yellow)}
.lead-rule{position:absolute;left:150px;top:170px;width:553px;height:3px;background:linear-gradient(90deg,transparent,var(--cyan),transparent)}
.title-en{position:absolute;left:0;top:190px;width:853px;text-align:center;font-family:var(--en);font-weight:900;font-size:150px;line-height:170px;letter-spacing:-4px;color:var(--cyan);text-shadow:0 0 18px rgba(53,198,244,.8),0 0 40px rgba(53,198,244,.5)}
.title-jp{position:absolute;left:200px;top:362px;width:630px;text-align:center;font-weight:900;font-size:46px;line-height:60px;color:var(--cyan-light);text-shadow:0 0 12px rgba(53,198,244,.7)}
.catch{position:absolute;left:45px;top:462px;writing-mode:vertical-rl;font-weight:900;font-size:34px;line-height:40px;letter-spacing:2px;text-shadow:0 2px 6px rgba(0,0,0,.8)}
.fee-badge{position:absolute;left:30px;top:845px;width:140px;height:140px;border-radius:50%;background:var(--pink);border:4px solid var(--white);text-align:center;box-shadow:0 4px 14px rgba(0,0,0,.5)}
.fee-badge .label{display:block;margin-top:26px;font-size:21px;font-weight:700}
.fee-badge .value{display:block;font-size:36px;font-weight:900;color:var(--yellow);line-height:46px}
.summary{position:absolute;left:355px;top:440px;width:470px;font-size:13.5px;line-height:22px;font-weight:500;background:rgba(5,11,30,.55);padding:4px 6px}
.period{position:absolute;left:355px;top:570px;display:flex;align-items:center;gap:10px}
.period .tag{background:var(--white);color:var(--blue);font-weight:900;font-size:16px;line-height:20px;width:52px;padding:5px 0;text-align:center}
.period .dates{color:var(--yellow);font-weight:900;font-size:26px;line-height:54px;white-space:nowrap}
.period .dates b{font-family:var(--en);font-size:52px}
.details{position:absolute;left:355px;top:636px;width:335px;font-size:12.5px;line-height:21px}
.details dt{display:inline-block;background:var(--cyan);color:var(--navy);font-weight:700;padding:0 6px;margin-right:6px}
.details dd{display:inline}
.scholarship{position:absolute;left:708px;top:636px;width:116px;height:116px;border-radius:50%;background:var(--white);text-align:center;color:var(--pink);box-shadow:0 4px 14px rgba(0,0,0,.5);padding-top:16px}
.scholarship .ribbon{display:block;font-size:11px;font-weight:700;line-height:16px}
.scholarship .word{display:block;font-size:20px;font-weight:900;line-height:28px;color:var(--blue)}
.scholarship .amount{display:block;font-size:24px;font-weight:900;line-height:30px}
.joint{position:absolute;left:355px;top:712px;background:var(--yellow);color:var(--navy);font-weight:900;font-size:20px;line-height:28px;padding:0 14px}
.program{position:absolute;left:355px;top:758px;width:470px;border-collapse:collapse}
.program th{width:66px;background:var(--blue);color:var(--white);font-size:14px;font-weight:900;height:38px;border:2px solid var(--navy)}
.program td{background:var(--white);color:var(--blue);font-size:15px;font-weight:900;line-height:19px;padding-left:8px;border:2px solid var(--navy);white-space:nowrap}
.program td small{display:block;font-size:10px;color:var(--ink);font-weight:500;line-height:12px}
.apply{position:absolute;left:355px;top:924px;width:470px;height:78px;background:rgba(255,255,255,.08);border:1px solid rgba(255,255,255,.3);padding:6px 8px;font-size:11px;line-height:16px}
.apply .head{display:inline-block;background:var(--pink);color:var(--white);font-weight:900;font-size:13px;padding:0 8px;margin-right:8px}
.apply .url{font-weight:700;color:var(--cyan-light)}
.footer{position:absolute;left:0;top:1010px;width:853px;height:190px;background:var(--white);color:var(--ink);padding:18px 40px}
.school{display:flex;align-items:center;gap:10px;font-weight:700}
.school .mark{width:26px;height:26px;background:var(--blue)}
.school .corp{font-size:16px}
.school .name{font-size:24px;font-weight:900;color:var(--blue)}
.contact{display:flex;align-items:center;gap:16px;margin-top:16px}
.contact .label{background:var(--pink);color:var(--white);font-weight:700;font-size:18px;padding:6px 12px}
.contact .tel{display:flex;align-items:center;gap:8px;font-family:var(--en);font-weight:900;font-size:54px;color:var(--blue);line-height:60px}
.contact .tel svg{width:44px;height:44px}
.sub-contact{margin-top:10px;font-size:15px;font-weight:500}
.sub-contact span{margin-right:30px}
</style>
</head>
<body>
<div class="flyer">
  <div class="hero-photo" role="img" aria-label="照明に照らされたeスポーツ大会の会場と、腕を組む若い男性プレイヤーの写真"></div>

  <p class="lead">eスポーツ分野の仕事に<br>興味のある<em>高校生</em>たちへ!</p>
  <div class="lead-rule"></div>

  <h1 class="title-en">e-Sports</h1>
  <h2 class="title-jp">マネジメント人材養成講座</h2>

  <p class="catch">新しい可能性に挑戦!</p>

  <div class="fee-badge"><span class="label">参加費</span><span class="value">無料!!</span></div>

  <p class="summary">未来ビジネス専門学校では、〇〇〇〇協会と合同でeスポーツ分野の人材育成を目的とした講座を開催します。eスポーツチームのマネジメントやイベント運営について、第一線で活躍する講師から直接学ぶことができます。入選者には奨学金を支給します。eスポーツ業界で働きたい高校生のみなさん、ぜひご参加ください。</p>

  <div class="period">
    <span class="tag">開催<br>期間</span>
    <span class="dates"><b>11</b>月上旬〜<b>12</b>月上旬 <b>1</b>か月間</span>
  </div>

  <dl class="details">
    <dt>対象</dt><dd>高校1〜3年生(eスポーツに興味のある方)</dd><br>
    <dt>場所</dt><dd>未来ビジネス専門学校 ○○駅から徒歩3分</dd><br>
    <dd>※上記期間内のうち2日間、各回2時間程度</dd>
  </dl>

  <div class="scholarship">
    <span class="ribbon">入選した人には</span>
    <span class="word">奨学金</span>
    <span class="amount">10万円</span>
  </div>

  <div class="joint">合同開催!</div>
  <table class="program">
    <tr><th>講座1</th><td>日本のeスポーツの概要とこれから<small>講師:○○○○ eスポーツ協会</small></td></tr>
    <tr><th>講座2</th><td>プロeスポーツチーム&amp;プレイヤーの活動<small>講師:○○○○ プロチーム代表</small></td></tr>
    <tr><th>実習</th><td>eスポーツチームマネジメント ケーススタディ学習</td></tr>
    <tr><th>実習</th><td>PBL学習<small>チームで課題を設定し解決策を発表</small></td></tr>
  </table>

  <div class="apply">
    <span class="head">申込方法</span>下記URLの申込フォームよりお申し込みください。<br>
    <span class="url">https://mirai-gakuin.example/esports</span><br>
    ※定員になり次第締め切ります。お早めにお申し込みください。<br>
    ※詳細は決定次第、申込者へメールでご連絡します。
  </div>

  <footer class="footer">
    <div class="school"><span class="mark"></span><span class="corp">学校法人 未来学園</span><span class="name">未来ビジネス専門学校 みらい学院</span></div>
    <div class="contact">
      <span class="label">お問合せ</span>
      <span class="tel">
        <svg viewBox="0 0 24 24" aria-hidden="true"><path fill="#0c5fb8" d="M6.6 10.8a15.1 15.1 0 0 0 6.6 6.6l2.2-2.2a1 1 0 0 1 1-.25 11.4 11.4 0 0 0 3.6.57 1 1 0 0 1 1 1V20a1 1 0 0 1-1 1A17 17 0 0 1 3 4a1 1 0 0 1 1-1h3.5a1 1 0 0 1 1 1c0 1.25.2 2.45.57 3.57a1 1 0 0 1-.25 1z"/></svg>
        000-000-0000
      </span>
    </div>
    <p class="sub-contact"><span>FAX:000-000-0000</span><span>メール:info@mirai-gakuin.example</span></p>
  </footer>
</div>
</body>
</html>
```